Quiet Ledger needs a book cover

Enabling people to find a new way of looking at money. If peoples thoughts, attitude and emotions around money are not inline with their goals and dreams then it is often harder to achieve their version of success.

Recognition that we have an emotional and a practical way with money.

Quiet Ledger enables people to find a sustainable (balanced) way with money for their life right now and their future.

Developing this over the years and seeing clients achieve a clear picture/idea/thought connection that is positive around money and it's purpose to them in their lives has truly been fabulous as they have then gone on to achieve their goals and dreams.

Title of book = Quiet Ledger
Tag line = Being healthy being wealthy
Authors Name = Ruth Pell
Book Size = 135 width x 185 height
Thumbnail = Cover must work well as well as full size
Looking for simple and clear app-able / icon type image
Feel free to have fun with it
A simple yet refreshing balanced, eye-catching design.

The back will include authors photo, blurb, testimonials, barcode, ISBN number & price. I will provide once front cover is sorted.

Reason: Realised that the tag line for the book was incorrect.

Target Market(s)

Individuals

Industry/Entity Type

Work

Requirements
Must have
• First work on front cover, once approved we can then do spine and back cover

```html
<!DOCTYPE html>
<html lang="en">
<head>
<meta charset="utf-8">
<title>Quiet Ledger — Ruth Pell</title>
<link href="https://fonts.googleapis.com/css2?family=Bebas+Neue&family=Arimo:wght@400;700&display=swap" rel="stylesheet">
<style>
  :root {
    --bg-light: #ececec;
    --bg-mid: #c9c9c9;
    --bg-dark: #939393;
    --author-white: #ffffff;
    --title-yellow: #f7d83c;
    --tagline-grey: #3a3a3a;
    --slot-line: #8c8c8c;
    --slot-shadow: rgba(255,255,255,0.6);
    --icon-blue-light: #5db8e6;
    --icon-blue-mid: #2f7fb8;
    --icon-blue-deep: #1c3f63;
  }
  * { margin: 0; padding: 0; box-sizing: border-box; }
  html, body { width: 874px; height: 1200px; overflow: hidden; background: var(--bg-mid); }
  .cover {
    position: relative;
    width: 874px;
    height: 1200px;
    overflow: hidden;
    background: radial-gradient(ellipse 75% 60% at 50% 42%, var(--bg-light) 0%, var(--bg-mid) 55%, var(--bg-dark) 100%);
  }
  .author {
    position: absolute;
    top: 58px;
    left: 0;
    width: 100%;
    text-align: center;
    font-family: "Arimo", sans-serif;
    font-size: 42px;
    line-height: 1.2;
    letter-spacing: 0.34em;
    padding-left: 0.34em;
    color: var(--author-white);
  }
  .money-art {
    position: absolute;
    left: 140px;
    top: 172px;
    width: 596px;
    height: 364px;
    border-radius: 50% 50% 0 0 / 60% 60% 0 0;
    background: radial-gradient(ellipse at 55% 65%, var(--icon-blue-deep) 0%, var(--icon-blue-mid) 45%, var(--icon-blue-light) 80%, rgba(93,184,230,0) 100%);
    opacity: 0.85;
  }
  .slot {
    position: absolute;
    left: 0;
    top: 530px;
    width: 874px;
    height: 12px;
  }
  .title {
    position: absolute;
    top: 592px;
    left: 0;
    width: 100%;
    text-align: center;
    font-family: "Bebas Neue", sans-serif;
    font-weight: 400;
    font-size: 280px;
    line-height: 0.83;
    color: var(--title-yellow);
  }
  .title span { display: block; }
  .tagline {
    position: absolute;
    top: 1074px;
    left: 0;
    width: 100%;
    text-align: center;
    font-family: "Arimo", sans-serif;
    font-size: 30px;
    line-height: 1.2;
    color: var(--tagline-grey);
  }
</style>
</head>
<body>
  <main class="cover">
    <p class="author">Ruth Pell</p>
    <div class="money-art" role="img" aria-label="Cluster of paper-cut dollar sign icons in shades of blue rising out of a slot"></div>
    <svg class="slot" viewBox="0 0 874 12" aria-hidden="true">
      <line x1="125" y1="5" x2="752" y2="5" stroke="var(--slot-line)" stroke-width="2"/>
      <line x1="125" y1="8" x2="752" y2="8" stroke="var(--slot-shadow)" stroke-width="2"/>
    </svg>
    <h1 class="title"><span>Quiet</span><span>Ledger</span></h1>
    <p class="tagline">Being healthy being wealthy</p>
  </main>
</body>
</html>
```